Boutique High End Custom Furniture Store, Client Appreciation Card

We are looking to create a 5 x 7 card for our best clients that offer a 15% discount on their next furniture purchase. We would like to use both sides, full colour.

We are a high-end boutique furniture store located in Calgary, AB, Canada.

I have attached a card we did for our grand reopening that we like -- it's fresh with lots of white space. I have attached the image we used as well as a possible second image of furniture.

I have also attached other examples -- all seem fresh and clean with a layer of luxury.

I have attached all versions of our logo in an EPS file.

Target Market(s)

High disposable income, women over 40 who love style, contemporary design and fine art. Think Lina Morrow, Finch Allard, Vera Quill perfume and http://www.marlowbey.example/

Industry/Entity Type

Boutique

Font styles to use
Sans Serif
Script

Colors
33a6d7
0592cd
85cae6
eda3c7
e667a6

Requirements
Must have
• Must be colour on both side (one side logo perhaps), the other side has content? Card needs to be 5 x 7 (either orientation is okay). Card needs to be fresh, stylish and current with the use of colour i.e. not all black and white. Logo needs to be prominent on either side.
• Please also have a look at our website.
Should not have
• Should not feel traditional or dated but at the same time not too playful so that it looks unprofessional. We are not "Hal's discount Sofas"!

```html
<!DOCTYPE html>
<html lang="en">
<head>
<meta charset="utf-8">
<title>Linden Loft – Client Appreciation Card</title>
<link rel="stylesheet" href="https://fonts.googleapis.com/css2?family=Josefin+Sans:wght@300;400;600;700&family=Montserrat:wght@600;700&family=Kaushan+Script&display=swap">
<style>
  :root {
    --backdrop: #c2c0c3;
    --paper: #ffffff;
    --pink: #e667a6;
    --pink-soft: #eda3c7;
    --ink-grey: #6d6d6d;
    --line-grey: #a9a9a9;
    --rule: #a9a9a9;
  }
  * { box-sizing: border-box; margin: 0; padding: 0; }
  html, body {
    width: 1200px; height: 1200px; overflow: hidden;
    background: var(--backdrop);
  }
  .canvas { position: relative; width: 1200px; height: 1200px; }

  .card {
    position: absolute;
    width: 553px; height: 774px;
    background: var(--paper);
    box-shadow: 0 2px 8px rgba(0,0,0,0.18);
    overflow: hidden;
  }
  .card--offer { left: 26px; top: 383px; }
  .card--brand { left: 611px; top: 41px; }

  /* Offer side */
  .offer-head { position: absolute; left: 0; top: 0; width: 100%; height: 281px; border-bottom: 2px solid var(--rule); }
  .enjoy-badge {
    position: absolute; left: 22px; top: 54px;
    width: 140px; height: 140px; border-radius: 50%;
    background: var(--pink);
    border: 4px solid var(--pink-soft);
    display: flex; align-items: center; justify-content: center;
    color: var(--paper);
    font-family: "Kaushan Script", cursive;
    font-size: 44px; transform: rotate(-6deg);
  }
  .offer-kicker, .offer-where {
    position: absolute; left: 176px;
    font-family: "Josefin Sans", sans-serif; font-weight: 300;
    color: var(--pink); font-size: 28px; letter-spacing: 7px;
    white-space: nowrap;
  }
  .offer-kicker { top: 54px; }
  .offer-where { top: 172px; font-size: 27px; letter-spacing: 6.5px; }
  .offer-amount {
    position: absolute; left: 172px; top: 80px;
    font-family: "Montserrat", sans-serif; font-weight: 700;
    color: var(--pink); font-size: 86px; letter-spacing: -3px; line-height: 1.1;
    white-space: nowrap;
  }
  .offer-amount sup { font-size: 24px; vertical-align: top; position: relative; top: 6px; margin-left: 6px; letter-spacing: 0; }
  .offer-terms {
    position: absolute; left: 0; top: 223px; width: 100%; text-align: center;
    font-family: "Josefin Sans", sans-serif; font-weight: 300; font-size: 12.5px; color: #444;
  }
  .contact-line {
    position: absolute; left: 0; width: 100%; text-align: center;
    font-family: "Josefin Sans", sans-serif; font-weight: 300;
    font-size: 12px; color: var(--line-grey); white-space: nowrap;
  }
  .card--offer .contact-line { top: 254px; }
  .offer-photo {
    position: absolute; left: 0; top: 283px; width: 100%; height: 491px;
    background: linear-gradient(180deg, #f2f2f0 0%, #ecebe8 50%, #c9bfb3 72%, #b9aea2 88%, #dcdbd9 100%);
  }
  .offer-web {
    position: absolute; left: 0; top: 733px; width: 100%; text-align: center;
    font-family: "Josefin Sans", sans-serif; font-size: 13px; color: var(--paper);
  }

  /* Brand side */
  .brand-panel { position: absolute; left: 0; top: 0; width: 100%; height: 435px; background: var(--pink); }
  .brand-band { position: absolute; left: 0; top: 435px; width: 100%; height: 10px; background: var(--pink-soft); }
  .brand-name {
    position: absolute; left: 0; top: 262px; width: 100%; text-align: center;
    font-family: "Josefin Sans", sans-serif; font-weight: 400;
    font-size: 48px; letter-spacing: 4px; text-transform: uppercase; color: var(--paper);
  }
  .brand-tagline {
    position: absolute; left: 0; top: 328px; width: 100%; text-align: center;
    font-family: "Josefin Sans", sans-serif; font-weight: 300;
    font-size: 22px; letter-spacing: 1px; color: var(--paper);
  }
  .brand-about {
    position: absolute; left: 108px; top: 534px; width: 337px; text-align: center;
    font-family: "Josefin Sans", sans-serif; font-size: 13px; line-height: 20px;
    text-transform: uppercase; color: var(--ink-grey);
  }
  .card--brand .contact-line { top: 730px; }
</style>
</head>
<body>
<main class="canvas">
  <section class="card card--offer" aria-label="Offer side">
    <div class="offer-head">
      <div class="enjoy-badge">Enjoy</div>
      <p class="offer-kicker">OUR GIFT TO YOU</p>
      <p class="offer-amount">15% OFF<sup>*</sup></p>
      <p class="offer-where">AT LINDEN LOFT</p>
      <p class="offer-terms">Offer is good for one-time use and cannot be combined with other offers.</p>
      <p class="contact-line">2210 LARKSPUR AVE SW, CALGARY AB | 403.555.0182 | INFO@LINDENLOFT.CA</p>
    </div>
    <div class="offer-photo" role="img" aria-label="Bright interior with a taupe sideboard, yellow vase of white lilies, framed abstract art, a wooden chair and a tan upholstered bench"></div>
    <p class="offer-web">LINDENLOFT.CA</p>
  </section>

  <section class="card card--brand" aria-label="Brand side">
    <div class="brand-panel">
      <h1 class="brand-name">Linden Loft</h1>
      <p class="brand-tagline">Furniture, art and quiet comfort</p>
    </div>
    <div class="brand-band"></div>
    <p class="brand-about">Linden Loft is a unique boutique custom furniture store offering a wide selection of furniture, rugs, bedding, lighting, window coverings, accessories and interior design services.</p>
    <p class="contact-line">2210 LARKSPUR AVE SW, CALGARY AB | 403.555.0182 | INFO@LINDENLOFT.CA</p>
  </section>
</main>
</body>
</html>
```